Crestline Inspection Partners Business Card Design

a specialised consulting company, aviation specialist, like to have use blue colour on white background.
back of card to have printed-
NDT Expertise:
INSPECTION & TESTING CONSULTING
TRAINING & EDUCATION
CERTIFICATION SERVICES
LEVEL 3 SERVICES
TARVOSK / AUDITING
INSPECTION SYSTEMS

Target Market(s)

Mainly the aerospace industry, manufacturers and airframe/engine overhaul companies.

Industry/Entity Type

Business

Contact Information for Business Card

Crestline Inspection Partners

Lionel Fairweather JP

+61 (0)437615042
crestlineinspection@mailbox-example.net

Font styles to use
Serif

Colors
3276b4
32a5d5

Requirements
Must have
• aviation style logo with letters CIP part of or adjacent to.

then company name: Crestline Inspection Partners

then name in slightly smaller font : Lionel Fairweather JP

then phone and email details

Back of card, as per brief, but all text to be centred

```html
<!DOCTYPE html>
<html lang="en">
<head>
<meta charset="utf-8">
<title>Crestline Inspection Partners – Business Card</title>
<link rel="stylesheet" href="https://fonts.googleapis.com/css2?family=Cabin:wght@400;500&family=Open+Sans:wght@400&display=swap">
<style>
  :root {
    --backdrop: #dfe5e5;
    --card: #ffffff;
    --blue-deep: #2a37bd;
    --blue-mid: #5b64cc;
    --blue-soft: #6b72d2;
    --blue-haze: #3540c2;
    --mark-grey: #4a4a55;
    --ink: #2b2b2b;
    --white: #ffffff;
  }
  * { margin: 0; padding: 0; box-sizing: border-box; }
  html, body {
    width: 851px; height: 1200px; overflow: hidden;
    background: var(--backdrop);
  }
  .stage { position: relative; width: 851px; height: 1200px; }

  .card {
    position: absolute; left: 197px; width: 457px;
    background: var(--card); overflow: hidden;
  }
  .card--front { top: 279px; height: 281px; }
  .card--back  { top: 640px; height: 282px; }

  .band {
    position: absolute; left: 0; top: 0; width: 100%;
    overflow: hidden;
  }
  .card--front .band {
    height: 113px;
    background: linear-gradient(90deg,
      var(--blue-deep) 0%, var(--blue-mid) 28%, var(--blue-soft) 55%,
      var(--blue-soft) 72%, var(--blue-deep) 100%);
  }
  .card--back .band { height: 114px; }

  .band__texture {
    position: absolute; inset: 0;
    background: linear-gradient(90deg,
      var(--blue-deep) 0%, var(--blue-haze) 50%, var(--blue-deep) 100%);
  }

  .brand-mark {
    position: absolute; left: 22px; top: 72px;
    display: flex; align-items: center; gap: 6px;
    font-family: "Cabin", sans-serif; font-weight: 500;
    font-size: 32px; color: var(--mark-grey); line-height: 1;
  }
  .brand-mark__square { width: 14px; height: 14px; background: var(--mark-grey); }

  .holder-name {
    position: absolute; right: 26px; top: 86px;
    font-family: "Cabin", sans-serif; font-weight: 400;
    font-size: 23px; color: var(--white); line-height: 1;
  }

  .contact {
    position: absolute; right: 26px; top: 198px; text-align: right;
    font-family: "Open Sans", sans-serif; font-style: normal; font-size: 13px;
    color: var(--ink); line-height: 18.5px;
  }

  .section-title {
    position: absolute; left: 0; width: 100%; top: 93px; text-align: center;
    font-family: "Cabin", sans-serif; font-weight: 400;
    font-size: 19px; color: var(--white); line-height: 1;
  }

  .services {
    position: absolute; left: 0; width: 100%; top: 134px;
    list-style: none; text-align: center;
    font-family: "Open Sans", sans-serif; font-size: 11.5px;
    color: var(--ink); line-height: 14.6px;
  }
</style>
</head>
<body>
<main class="stage">

  <section class="card card--front" aria-label="Business card front">
    <div class="band">
      <div class="brand-mark"><span class="brand-mark__square"></span>CIP</div>
      <h1 class="holder-name">Lionel Fairweather JP</h1>
    </div>
    <address class="contact">
      Crestline Inspection Partners<br>
      +61 (0)437615042<br>
      crestlineinspection@mailbox-example.net
    </address>
  </section>

  <section class="card card--back" aria-label="Business card back">
    <div class="band">
      <div class="band__texture" role="img" aria-label="Decorative band of faint repeating service names on blue"></div>
      <h2 class="section-title">NDT Expertise</h2>
    </div>
    <ul class="services">
      <li>Inspection &amp; Testing Consulting</li>
      <li>Training &amp; Education</li>
      <li>Certification Services</li>
      <li>Level 3 Services</li>
      <li>TARVOSK / Auditing</li>
      <li>Inspection Systems</li>
    </ul>
  </section>

</main>
</body>
</html>
```